Navelo Partnering Business Card

Hello everyone. We need a business card design that would match our logo and the theme we're trying to have for Navelo that you can find on our website and/or Corvapage page

```html
<!DOCTYPE html>
<html lang="en">
<head>
<meta charset="utf-8">
<title>Navelo Partnering Business Card</title>
<link rel="stylesheet" href="https://fonts.googleapis.com/css2?family=Jost:wght@400;600&family=Work+Sans:wght@400;600&display=swap">
<style>
  :root {
    --backdrop: #161616;
    --card: #232323;
    --card-edge: #2c2c2c;
    --foil: #d6d6d6;
    --foil-soft: #b9b9b9;
    --emboss: #151515;
    --divider: #5a5a5a;
  }
  * { margin: 0; padding: 0; box-sizing: border-box; }
  html, body {
    width: 1200px;
    height: 900px;
    overflow: hidden;
    background: var(--backdrop);
  }
  .canvas {
    position: relative;
    width: 1200px;
    height: 900px;
    background: radial-gradient(ellipse at 60% 35%, #262626 0%, var(--backdrop) 70%);
  }
  .card {
    position: absolute;
    left: 280px;
    width: 640px;
    height: 366px;
    background: var(--card);
    border: 1px solid var(--card-edge);
  }
  .card--front { top: 64px; }
  .card--back { top: 468px; }

  .brand-name {
    font-family: "Work Sans", sans-serif;
    font-weight: 600;
    letter-spacing: 0.5px;
    white-space: nowrap;
  }
  .card--front .brand-name {
    position: absolute;
    top: 128px;
    left: 0;
    width: 100%;
    text-align: center;
    font-size: 46px;
    color: var(--foil);
  }
  .front-web {
    position: absolute;
    bottom: 34px;
    left: 0;
    width: 100%;
    text-align: center;
    font-family: "Work Sans", sans-serif;
    font-size: 15px;
    letter-spacing: 0.8px;
    color: var(--emboss);
  }

  .card--back .brand-name {
    position: absolute;
    top: 146px;
    left: 40px;
    width: 230px;
    text-align: center;
    font-size: 30px;
    line-height: 1.15;
    color: var(--emboss);
    white-space: normal;
  }
  .back-divider {
    position: absolute;
    left: 298px;
    top: 88px;
    width: 1px;
    height: 190px;
    background: var(--divider);
  }
  .contact {
    position: absolute;
    left: 334px;
    top: 78px;
    color: var(--foil);
    font-family: "Work Sans", sans-serif;
  }
  .contact__name {
    font-family: "Jost", sans-serif;
    font-weight: 600;
    font-size: 25px;
    letter-spacing: 1.8px;
    text-transform: uppercase;
    line-height: 1;
  }
  .contact__role {
    font-family: "Jost", sans-serif;
    font-size: 16px;
    color: var(--foil-soft);
    margin-top: 2px;
    letter-spacing: 0.5px;
  }
  .contact__address {
    margin-top: 22px;
    font-size: 15px;
    line-height: 1.35;
    letter-spacing: 0.8px;
  }
  .contact__list {
    list-style: none;
    margin-top: 12px;
    font-size: 15px;
    letter-spacing: 0.8px;
  }
  .contact__list li {
    display: flex;
    align-items: center;
    gap: 10px;
    height: 24px;
  }
  .contact__list svg {
    width: 12px;
    height: 12px;
    flex: none;
  }
</style>
</head>
<body>
<main class="canvas">
  <section class="card card--front" aria-label="Card front">
    <div class="brand-name">Navelo Partnering</div>
    <div class="front-web">www.navelopartnering.com</div>
  </section>

  <section class="card card--back" aria-label="Card back">
    <div class="brand-name">Navelo Partnering</div>
    <div class="back-divider"></div>
    <div class="contact">
      <div class="contact__name">Daniel Reyes</div>
      <div class="contact__role">Founder</div>
      <div class="contact__address">2840 N. Harbor Ave.<br>Coral Bay, FL 33071</div>
      <ul class="contact__list">
        <li>
          <svg viewBox="0 0 12 12" aria-hidden="true"><path d="M2.5 1 L4.5 1 L5.3 3.5 L4 4.5 C4.6 6 6 7.4 7.5 8 L8.5 6.7 L11 7.5 L11 9.5 C11 10.3 10.3 11 9.5 11 C5 11 1 7 1 2.5 C1 1.7 1.7 1 2.5 1 Z" fill="#cfcfcf"/></svg>
          555-318-2046
        </li>
        <li>
          <svg viewBox="0 0 12 12" aria-hidden="true"><rect x="0.8" y="2.5" width="10.4" height="7" fill="none" stroke="#cfcfcf" stroke-width="1.2"/><path d="M1 3 L6 6.8 L11 3" fill="none" stroke="#cfcfcf" stroke-width="1.2"/></svg>
          info@navelopartnering.com
        </li>
        <li>
          <svg viewBox="0 0 12 12" aria-hidden="true"><circle cx="6" cy="6" r="5" fill="none" stroke="#cfcfcf" stroke-width="1.1"/><ellipse cx="6" cy="6" rx="2.2" ry="5" fill="none" stroke="#cfcfcf" stroke-width="1"/><path d="M1 6 H11" stroke="#cfcfcf" stroke-width="1"/></svg>
          www.navelopartnering.com
        </li>
      </ul>
    </div>
  </section>
</main>
</body>
</html>
```